Letterhead Surgical Clinic ,Perth- Australia

We need a letterhead for our surgical clinic , it needs to highlight all the relevant contact details and practice locations. needs to be eye catching, but remain professional.all the logos attached
clear contact details as follows

Surgeon name : Mr Tesin Varoque
Phone : 1300 482 917 - 0412 938 264
Fax : 08- 7429 5830
email : tesin@glandcarepractice.com.au
www.glandcarepractice.com.au

Consults from
1- Calloway Medical Centre - Level 3 - Suite 42.
9 Quenton Hale Boulevard
Brennock WA 6177

2- HKOV Mandurah Suites
241 Pellridge Road Calderwyn 6290

Operates at :
Holy Keel of Valour Murdoch Hospital
Greta Olwick Hospital
Tarn Health Campus
Corriwell Hospital
Dunmarsh Hopital
Holy Keel of Valour Subiaco

Target Market(s)

General Practitioners (Family doctors)

Industry/Entity Type

Medical

Requirements
Must have
• all the logos attached
• clear contact details as follows
• Surgeon name : Mr Tesin Varoque
• Phone : 1300 482 917 - 0412 938 264
• Fax : 08- 7429 5830
• email : tesin@glandcarepractice.com.au
• www.glandcarepractice.com.au
• Consults from
• 1- Calloway Medical Centre - Level 3 - Suite 42.
• 9 Quenton Hale Boulevard
• Brennock WA 6177
• 2- HKOV Mandurah Suites
• 241 Pellridge Road Calderwyn 6290
• Operates at :
• Holy Keel of Valour Murdoch Hospital
• Greta Olwick Hospital
• Tarn Health Campus
• Corriwell Hospital
• Dunmarsh Hopital
• Holy Keel of Valour Subiaco
Nice to have
• a surgical theme in the design , but remain professional
Should not have
• big chunky designs
• no photographs or diagrams of objects (ECG, or stethoscope ..ect)

```html
<!DOCTYPE html>
<html lang="en">
<head>
<meta charset="utf-8">
<title>Letterhead – Mr Tesin Varoque, Surgeon</title>
<link rel="stylesheet" href="https://fonts.googleapis.com/css2?family=Open+Sans:wght@400;600;700;800&display=swap">
<style>
  :root {
    --brand-blue: #2f5fc4;
    --brand-dark: #3b3d4a;
    --paper: #f5f5f5;
    --stage: #e6e7ea;
    --badge: #c9ccd3;
    --mark-faint: #dcdcdc;
    --white: #ffffff;
  }
  * { box-sizing: border-box; margin: 0; padding: 0; }
  html, body {
    width: 1200px; height: 675px; overflow: hidden;
    background: var(--stage);
    font-family: "Open Sans", Arial, sans-serif;
  }
  .letterhead {
    position: absolute; left: 373px; top: 17px;
    width: 453px; height: 640px;
    background: var(--paper);
    box-shadow: 0 2px 10px rgba(0,0,0,0.12);
    overflow: hidden;
  }
  .letterhead-shapes { position: absolute; inset: 0; }

  .header-block {
    position: absolute; right: 14px; top: 8px;
    text-align: right; color: var(--white);
  }
  .header-role { font-size: 7px; font-weight: 800; letter-spacing: 0.5px; }
  .header-name { font-size: 12px; font-weight: 700; line-height: 1.1; }
  .header-contact { font-size: 5.6px; line-height: 1.55; margin-top: 3px; }
  .header-contact .sep { margin: 0 3px; }

  .watermark-mark {
    position: absolute; left: 120px; top: 150px;
    display: flex; align-items: center; gap: 10px;
    font-size: 34px; font-weight: 700; color: var(--mark-faint);
  }
  .watermark-mark .mark-dot {
    width: 30px; height: 30px; border-radius: 50%; background: var(--mark-faint);
  }

  .footer-heading {
    font-size: 7px; font-weight: 800; color: var(--white);
    letter-spacing: 0.3px; margin-bottom: 3px;
  }
  .footer-list { list-style: none; color: var(--white); font-size: 5.6px; line-height: 1.45; }
  .footer-list li { position: relative; padding-left: 8px; }
  .footer-list li::before {
    content: ""; position: absolute; left: 0; top: 2.6px;
    width: 3.5px; height: 3.5px; border-radius: 50%; background: var(--white);
  }
  .consults-from { position: absolute; left: 16px; top: 544px; width: 150px; }
  .operates-at { position: absolute; left: 176px; top: 552px; width: 130px; }
  .operates-at-more { position: absolute; left: 318px; top: 572px; width: 130px; }

  .accreditation-row {
    position: absolute; left: 16px; right: 16px; top: 606px; height: 18px;
    display: flex; align-items: center; justify-content: space-between;
  }
  .badge { background: var(--badge); }
  .badge.round { width: 14px; height: 14px; border-radius: 50%; }
  .badge.square { width: 14px; height: 14px; }
  .badge.wide { width: 34px; height: 10px; border-radius: 2px; }
</style>
</head>
<body>
  <main class="letterhead">
    <svg class="letterhead-shapes" viewBox="0 0 453 640" width="453" height="640" aria-hidden="true">
      <polygon points="0,0 453,0 453,76 206,76 194,58 0,58" fill="var(--brand-blue)"/>
      <path d="M0,63 H186 L197,78" fill="none" stroke="var(--brand-dark)" stroke-width="3"/>
      <polygon points="0,536 280,536 292,554 453,554 453,600 0,600" fill="var(--brand-blue)"/>
      <path d="M296,548 H453" fill="none" stroke="var(--brand-dark)" stroke-width="3"/>
      <rect x="0" y="629" width="453" height="11" fill="var(--brand-dark)"/>
    </svg>

    <header class="header-block">
      <p class="header-role">SURGEON</p>
      <h1 class="header-name">Mr Tesin Varoque</h1>
      <p class="header-contact">
        Phone : 1300 482 917<span class="sep">|</span>Phone : 0412 938 264<span class="sep">|</span>Fax : 08- 7429 5830<br>
        tesin@glandcarepractice.com.au<span class="sep">|</span>www.glandcarepractice.com.au
      </p>
    </header>

    <div class="watermark-mark" role="img" aria-label="Glandcare Practice mark">
      <span class="mark-dot"></span>Glandcare
    </div>

    <section class="consults-from">
      <h2 class="footer-heading">CONSULTS FROM</h2>
      <ul class="footer-list">
        <li>Calloway Medical Centre - Level 3 - Suite 42.<br>9 Quenton Hale Boulevard, Brennock WA 6177</li>
        <li>HKOV Mandurah Suites<br>241 Pellridge Road, Calderwyn 6290</li>
      </ul>
    </section>

    <section class="operates-at">
      <h2 class="footer-heading">OPERATES AT</h2>
      <ul class="footer-list">
        <li>Holy Keel of Valour Murdoch Hospital</li>
        <li>Greta Olwick Hospital</li>
        <li>Tarn Health Campus</li>
        <li>Corriwell Hospital</li>
      </ul>
    </section>
    <ul class="footer-list operates-at-more">
      <li>Dunmarsh Hopital</li>
      <li>Holy Keel of Valour Subiaco</li>
    </ul>

    <div class="accreditation-row" aria-label="Professional affiliations">
      <span class="badge round"></span>
      <span class="badge wide"></span>
      <span class="badge square"></span>
      <span class="badge wide"></span>
      <span class="badge round"></span>
      <span class="badge wide"></span>
      <span class="badge square"></span>
      <span class="badge wide"></span>
      <span class="badge round"></span>
      <span class="badge square"></span>
    </div>
  </main>
</body>
</html>
```